Need a book cover design for book titled: Resting Beside the River--Simple Methods for the Crossing

This book describes and presents tools to connect with and activate the Lightbody that we all carry within us. It talks about the Lighbody, brief history, lightbody levels and offers exercises to bring light into the body.
I envision a design that shows a physical body changing into light /surrounded by light; a resurrected body ascending to higher dimensions of Spirit o anything comparable .
Updates

Target Market(s)

Mature audience of spiritual seekers and those on spiritual path

Requirements
Must have
• Space on backcover for book summary at top and title and author name on spine.

```html
<!DOCTYPE html>
<html lang="en">
<head>
<meta charset="utf-8">
<title>Resting Beside the River — Book Cover Wrap</title>
<link rel="stylesheet" href="https://fonts.googleapis.com/css2?family=Marcellus&family=Tinos&display=swap">
<style>
  :root {
    --page: #ffffff;
    --cover-teal: #92ccd6;
    --cover-deep: #6fa7b1;
    --glow: #dff3fb;
    --sky: #bfe3f5;
    --title-ink: #2f6b6a;
    --body-ink: #1f3a40;
    --photo-box: #c5e4ea;
    --seam: #5d8f98;
  }
  * { box-sizing: border-box; margin: 0; padding: 0; }
  html, body { width: 775px; height: 1200px; overflow: hidden; background: var(--page); }
  .canvas { position: relative; width: 775px; height: 1200px; }

  .wrap {
    position: absolute; left: 34px; top: 339px;
    width: 706px; height: 522px;
    background: var(--cover-teal);
  }

  .back { position: absolute; left: 0; top: 0; width: 336px; height: 100%; }
  .back-title {
    position: absolute; left: 0; top: 44px; width: 342px;
    font-family: "Marcellus", serif; font-size: 15px; line-height: 19.3px;
    color: var(--title-ink); text-align: center; text-transform: uppercase;
  }
  .summary {
    position: absolute; left: 30px; top: 133px; width: 283px;
    font-family: "Tinos", serif; font-size: 6.3px; line-height: 8.4px;
    color: var(--body-ink); text-align: justify; hyphens: auto;
  }
  .summary p + p { margin-top: 8.4px; }
  .author-photo {
    position: absolute; left: 35px; top: 312px; width: 65px; height: 80px;
    background: var(--photo-box);
  }
  .author-bio {
    position: absolute; left: 113px; top: 311px; width: 200px;
    font-family: "Tinos", serif; font-size: 6.3px; line-height: 8.4px;
    color: var(--body-ink); text-align: justify; hyphens: auto;
  }
  .code-space {
    position: absolute; left: 203px; top: 433px; width: 105px; height: 40px;
    background: #ffffff;
  }

  .spine {
    position: absolute; left: 336px; top: 0; width: 34px; height: 100%;
    border-left: 1px solid var(--seam); border-right: 1px solid var(--seam);
  }
  .spine-text {
    position: absolute; left: 9px; top: 38px;
    writing-mode: vertical-rl;
    font-family: "Marcellus", serif; font-size: 10.5px; letter-spacing: 0.2px;
    color: var(--body-ink); text-transform: uppercase; white-space: nowrap;
  }
  .spine-text .spine-author { margin-top: 10px; }

  .front {
    position: absolute; left: 370px; top: 0; width: 336px; height: 100%;
    background:
      radial-gradient(ellipse 45% 60% at 50% 10%, var(--sky) 0%, rgba(191,227,245,0) 100%),
      radial-gradient(ellipse 30% 22% at 8% 70%, var(--cover-deep) 0%, rgba(111,167,177,0) 100%),
      radial-gradient(ellipse 30% 22% at 95% 62%, var(--cover-deep) 0%, rgba(111,167,177,0) 100%),
      var(--cover-teal);
    overflow: hidden;
  }
  .ascending-figure {
    position: absolute; left: 60px; top: 215px; width: 215px; height: 240px;
    background: radial-gradient(ellipse 50% 50% at 50% 55%, #f7fbfc 0%, var(--glow) 40%, rgba(223,243,251,0) 100%);
  }
  .front-title {
    position: absolute; left: 0; top: 38px; width: 100%;
    font-family: "Marcellus", serif; font-size: 30px; line-height: 34.3px;
    color: var(--title-ink); text-align: center; text-transform: uppercase;
  }
  .front-author {
    position: absolute; left: 0; top: 468px; width: 100%;
    font-family: "Marcellus", serif; font-size: 18px;
    color: var(--title-ink); text-align: center; text-transform: uppercase;
  }
</style>
</head>
<body>
<div class="canvas">
  <div class="wrap">
    <section class="back">
      <h2 class="back-title">Resting Beside the<br>River-Simple<br>Methods for<br>the Crossing</h2>
      <div class="summary">
        <p>Lorem ipsum dolor sit amet, consectetur adipiscing elit. Mauris congue orci vitae sapien auctor, et laoreet tellus egestas. Donec suscipit porta dui sed tempor. Class aptent taciti sociosqu ad litora torquent per conubia nostra, per inceptos himenaeos. Fusce non turpis sit amet nunc laoreet pharetra. Integer eu diam in metus posuere malesuada. Maecenas pharetra risus a nulla varius, ac dignissim felis egestas. Curabitur bibendum lectus vel diam facilisis sodales. Morbi velit purus, porta non euismod non, elementum quis justo. Duis non dapibus metus, eu congue tellus. Mauris pulvinar hendrerit orci.</p>
        <p>Sed molestie dui vel mollis pulvinar. Ut ac mi sem. Duis elementum massa metus, ac tempor nisl malesuada sit amet. Fusce auctor feugiat sapien sit amet dignissim. Maecenas sit amet semper neque. Donec sodales, augue vel interdum posuere, justo leo auctor eros, sed vulputate felis felis non ipsum. Cras sit amet consequat mauris. Sed ex metus, rutrum vitae vulputate et, elementum sed sapien.</p>
        <p>Vestibulum vel odio vel arcu efficitur cursus id in augue. Donec eu pharetra erat, at aliquet magna. Morbi scelerisque viverra venenatis. Curabitur justo massa, aliquam eu dolor a, egestas vehicula libero. Nunc consequat tincidunt neque sed porttitor. Curabitur in aliquet mauris. Vivamus at viverra eros. Vivamus est est, aliquam sed tempor at,</p>
      </div>
      <div class="author-photo" role="img" aria-label="Author portrait placeholder"></div>
      <p class="author-bio">Vestibulum vel odio vel arcu efficitur cursus id in augue. Donec eu pharetra erat, at aliquet magna. Morbi scelerisque viverra venenatis. Curabitur justo massa, aliquam eu dolor a, egestas vehicula libero. Nunc consequat tincidunt neque sed porttitor. Curabitur in aliquet mauris. Vivamus at viverra eros. Vivamus est est, aliquam sed tempor at, aliquam eu nulla. Aliquam ante enim, suscipit vel tellus ac, fringilla imperdiet metus. Duis sollicitudin finibus sapien, at venenatis dolor molestie in. Nulla malesuada, dolor id tempus scelerisque, augue odio vehicula urna, et pharetra velit libero ut risus. Quisque id tempor felis. Donec at consectetur eros.</p>
      <div class="code-space"></div>
    </section>

    <section class="spine">
      <p class="spine-text"><span>Resting Beside the River-Simple Methods for the Crossing</span><span class="spine-author">Author's Name</span></p>
    </section>

    <section class="front">
      <div class="ascending-figure" role="img" aria-label="Meditating figure in white dissolving into light, with rays rising upward from a glowing ring"></div>
      <h1 class="front-title">Resting<br>Beside the<br>River-Simple<br>Methods for<br>the Crossing</h1>
      <p class="front-author">Author's Name</p>
    </section>
  </div>
</div>
</body>
</html>
```